Verdant Loop Advisors, LLC

I am looking for a simple, clear layout with my logo prominent and embossed, on the best quality card stock available. I would like the business name and phone number included on the card as well......I dont want my name anywhere on the card and I would like my logo embossed on the card......something simple with a white back......open to designs as long as they go along with recycling symbols and green type stuff.....The address, website, cell number, fax number, and email are listed below

5374 Tillbury Fenwood Road
Brantholm, MD 20799

c. 240.555.0143 f. 240.555.0187
e. sales@verdantloopadvisors.example
w. www.verdantloopadvisors.example

Industry/Entity Type

Recycling

```html
<!DOCTYPE html>
<html lang="en">
<head>
<meta charset="utf-8">
<title>Verdant Loop Advisors, LLC — Business Card</title>
<link rel="stylesheet" href="https://fonts.googleapis.com/css2?family=Orbitron:wght@400&display=swap">
<style>
  :root {
    --paper: #ffffff;
    --ink: #1e1e1e;
    --leaf: #2e7d1f;
    --rule: #222222;
  }
  html, body {
    margin: 0;
    padding: 0;
    width: 1200px;
    height: 702px;
    overflow: hidden;
    background: var(--paper);
  }
  .card {
    position: relative;
    width: 1200px;
    height: 702px;
    background: var(--paper);
    color: var(--ink);
    font-family: "Orbitron", sans-serif;
    font-weight: 400;
  }
  .brand {
    position: absolute;
    top: 291px;
    left: 0;
    width: 1200px;
    display: flex;
    justify-content: center;
    align-items: center;
    gap: 18px;
  }
  .brand-mark {
    width: 38px;
    height: 38px;
    background: var(--leaf);
  }
  .brand-name {
    font-size: 25px;
    letter-spacing: 1px;
    text-transform: uppercase;
    color: var(--ink);
    white-space: nowrap;
  }
  .divider {
    position: absolute;
    top: 432px;
    left: 220px;
    width: 774px;
    border-top: 2px dotted var(--rule);
  }
  .address {
    position: absolute;
    top: 462px;
    left: 0;
    width: 1200px;
    margin: 0;
    text-align: center;
    font-style: normal;
    font-size: 25px;
    line-height: 35px;
    letter-spacing: 0.5px;
  }
  .phones, .online {
    position: absolute;
    margin: 0;
    padding: 0;
    list-style: none;
    letter-spacing: 0.5px;
  }
  .phones {
    top: 600px;
    left: 53px;
    font-size: 19px;
    line-height: 32px;
  }
  .online {
    top: 594px;
    right: 50px;
    font-size: 18px;
    line-height: 36px;
  }
</style>
</head>
<body>
  <main class="card">
    <div class="brand">
      <span class="brand-mark" aria-hidden="true"></span>
      <span class="brand-name">Verdant Loop Advisors, LLC</span>
    </div>

    <div class="divider" aria-hidden="true"></div>

    <address class="address">
      5374 tillbury fenwood road<br>
      Brantholm, md 20799
    </address>

    <ul class="phones">
      <li>TEL: 240.555.0143</li>
      <li>fax : 240.555.0187</li>
    </ul>

    <ul class="online">
      <li>w. www.verdantloopadvisors.example</li>
      <li>e. sales@verdantloopadvisors.example</li>
    </ul>
  </main>
</body>
</html>
```